Label for beer can

I need a new label for my beer cans which will be printed on the cans.
See the detailed description in "Description_PDF".

I would like to extend the deadline.

```html
<!DOCTYPE html>
<html lang="de">
<head>
<meta charset="utf-8">
<title>Blondes Lager – Dosenetikett</title>
<link rel="stylesheet" href="https://fonts.googleapis.com/css2?family=Oswald:wght@400;500;700&display=swap">
<style>
  :root {
    --backdrop: #e2e2e2;
    --label-black: #0b0b0b;
    --label-yellow: #fbf21a;
    --accent-orange: #f5b820;
    --brand-white: #ffffff;
    --ink: #111111;
  }
  html, body {
    margin: 0;
    padding: 0;
    width: 1200px;
    height: 800px;
    overflow: hidden;
    background: var(--backdrop);
  }
  .canvas {
    position: relative;
    width: 1200px;
    height: 800px;
  }
  .can-label {
    position: absolute;
    left: 450px;
    top: 25px;
    width: 300px;
    height: 750px;
    box-shadow: 0 10px 30px rgba(0,0,0,0.18);
  }
  .brand-name {
    font-family: "Oswald", sans-serif;
    font-weight: 700;
    font-size: 25px;
    fill: var(--brand-white);
    letter-spacing: 0.5px;
  }
  .style-name {
    font-family: "Oswald", sans-serif;
    font-weight: 700;
    font-size: 94px;
  }
  .style-name--blondes { fill: var(--label-yellow); }
  .style-name--lager { fill: var(--ink); }
  .facts {
    font-family: "Oswald", sans-serif;
    font-weight: 400;
    font-size: 11px;
    fill: var(--ink);
  }
  .facts--origin {
    font-weight: 500;
    font-size: 10px;
    letter-spacing: 0.4px;
  }
  .claim {
    font-family: "Oswald", sans-serif;
    font-weight: 500;
    font-size: 12px;
    letter-spacing: 0.6px;
    fill: var(--ink);
  }
</style>
</head>
<body>
<main class="canvas">
  <svg class="can-label" viewBox="0 0 300 750" xmlns="http://www.w3.org/2000/svg" aria-label="Blondes Lager Dosenetikett">
    <defs>
      <clipPath id="label-edge"><rect x="0" y="0" width="300" height="750"/></clipPath>
    </defs>
    <g clip-path="url(#label-edge)">
      <rect class="field-black" x="0" y="0" width="300" height="750" fill="var(--label-black)"/>
      <polygon class="field-yellow" points="300,53 300,750 0,750 0,606" fill="var(--label-yellow)"/>

      <g class="speed-lines" stroke="var(--label-yellow)" stroke-width="1.4" opacity="0.75">
        <line x1="100" y1="96" x2="-4" y2="296"/>
        <line x1="106" y1="98" x2="2" y2="298"/>
        <line x1="112" y1="100" x2="8" y2="300"/>
        <line x1="118" y1="102" x2="14" y2="302"/>
      </g>

      <g class="accent-lines" stroke="var(--accent-orange)" stroke-width="1.2" opacity="0.8">
        <line x1="298" y1="130" x2="262" y2="196"/>
        <line x1="300" y1="300" x2="262" y2="370"/>
        <line x1="150" y1="610" x2="118" y2="670"/>
        <line x1="156" y1="612" x2="124" y2="672"/>
      </g>

      <g class="brand">
        <circle cx="82" cy="39" r="5" fill="var(--label-yellow)"/>
        <text class="brand-name" x="152" y="49" text-anchor="middle">LUKABIER</text>
      </g>

      <text class="style-name style-name--blondes" transform="translate(62 480) rotate(-61.5)"
            x="0" y="0" textLength="410" lengthAdjust="spacingAndGlyphs">BLONDES</text>
      <text class="style-name style-name--lager" transform="translate(157 527) rotate(-61.5)"
            x="0" y="0" textLength="290" lengthAdjust="spacingAndGlyphs">LAGER</text>

      <g class="fact-block">
        <text class="facts" x="180" y="636" text-anchor="middle">5% ALC</text>
        <line x1="215" y1="625" x2="215" y2="640" stroke="var(--ink)" stroke-width="0.9"/>
        <text class="facts" x="248" y="636" text-anchor="middle">440 ML</text>
        <line x1="159" y1="645" x2="272" y2="645" stroke="var(--ink)" stroke-width="0.9"/>
        <text class="facts facts--origin" x="215" y="659" text-anchor="middle">SWISS CRAFT BEER</text>
      </g>

      <text class="claim" x="152" y="712" text-anchor="middle">NATURBELASSEN UND UNPASTEURISIERT</text>
    </g>
  </svg>
</main>
</body>
</html>
```